Lantern Business Cards

Need business cards for my employees at my restaurant.

Needs to include:
Our Logo
Lantern Bowls & Brews
Name: Nora Pettigrew
Title : Owner
Address: 487 Mirella Ave. Lake Havasu City, AZ 86519
Web: www.lanternkestrel.com
Phone: 928-555-0147
Cell: 928-555-0192
Email: info@lanternkestrel.com

```html
<!DOCTYPE html>
<html lang="en">
<head>
<meta charset="utf-8">
<title>Lantern Bowls &amp; Brews – Business Card</title>
<link rel="stylesheet" href="https://fonts.googleapis.com/css2?family=Montserrat:wght@600;700&family=Roboto:wght@400&display=swap">
<style>
  :root {
    --backdrop: #5a5a5a;
    --paper: #ffffff;
    --brand-red: #c01f2f;
    --ink: #4a4a4a;
    --rule: #c9c9c9;
    --ghost: #f2f2f2;
    --reverse: #262626;
    --reverse-light: #ffffff;
  }
  * { margin: 0; padding: 0; box-sizing: border-box; }
  html, body { width: 1200px; height: 1200px; overflow: hidden; }
  body { background: var(--backdrop); position: relative; font-family: "Roboto", Arial, sans-serif; }

  .card { position: absolute; width: 690px; height: 394px; overflow: hidden; }
  .card--front { left: 266px; top: 158px; background: var(--paper); }
  .card--back { left: 260px; top: 651px; background: var(--reverse); }

  .front__ghost {
    position: absolute; left: -14px; top: 32px; width: 340px; height: 340px;
    border-radius: 50%; background: var(--ghost);
  }

  .brand { position: absolute; left: 330px; top: 52px; display: flex; align-items: center; gap: 14px; }
  .brand__dot { width: 40px; height: 40px; border-radius: 50%; background: var(--brand-red); }
  .brand__name {
    font-family: "Montserrat", Arial, sans-serif; font-weight: 700;
    font-size: 27px; color: var(--brand-red); letter-spacing: 0.3px;
  }

  .person { position: absolute; left: 48px; top: 222px; }
  .person__name {
    font-family: "Montserrat", Arial, sans-serif; font-weight: 700;
    font-size: 27px; line-height: 30px; color: var(--brand-red);
  }
  .person__title { font-size: 15.5px; color: var(--ink); margin-top: 1px; }

  .divider { position: absolute; left: 48px; top: 281px; width: 592px; height: 1px; background: var(--rule); }

  .contact { position: absolute; left: 46px; top: 290px; list-style: none; }
  .contact__item { display: flex; align-items: center; height: 20.5px; font-size: 16.5px; color: var(--ink); }
  .contact__icon { width: 16px; height: 16px; margin-right: 8px; fill: var(--brand-red); }

  .address {
    position: absolute; right: 44px; top: 292px; text-align: right;
    font-size: 16.5px; line-height: 20.5px; color: var(--ink);
  }

  .back__pattern { position: absolute; inset: 0; background: linear-gradient(90deg, #1f1f1f, #2e2e2e); }
  .back__mark {
    position: absolute; left: 574px; top: 296px;
    font-family: "Montserrat", Arial, sans-serif; font-weight: 700;
    font-size: 14px; color: var(--reverse-light);
  }
</style>
</head>
<body>
  <section class="card card--front">
    <div class="front__ghost"></div>

    <div class="brand">
      <span class="brand__dot"></span>
      <span class="brand__name">Lantern Bowls &amp; Brews</span>
    </div>

    <div class="person">
      <h1 class="person__name">Nora Pettigrew</h1>
      <p class="person__title">Owner</p>
    </div>

    <div class="divider"></div>

    <ul class="contact">
      <li class="contact__item">
        <svg class="contact__icon" viewBox="0 0 24 24" aria-hidden="true"><path d="M6.6 10.8c1.4 2.8 3.8 5.1 6.6 6.6l2.2-2.2c.3-.3.7-.4 1-.2 1.1.4 2.3.6 3.6.6.6 0 1 .4 1 1V20c0 .6-.4 1-1 1C10.6 21 3 13.4 3 4c0-.6.4-1 1-1h3.5c.6 0 1 .4 1 1 0 1.3.2 2.5.6 3.6.1.3 0 .7-.2 1L6.6 10.8z"/></svg>
        928-555-0147
      </li>
      <li class="contact__item">
        <svg class="contact__icon" viewBox="0 0 24 24" aria-hidden="true"><path d="M7 1h10a2 2 0 0 1 2 2v18a2 2 0 0 1-2 2H7a2 2 0 0 1-2-2V3a2 2 0 0 1 2-2zm0 3v14h10V4H7zm5 15.2a1 1 0 1 0 0 2 1 1 0 0 0 0-2z"/></svg>
        928-555-0192
      </li>
      <li class="contact__item">
        <svg class="contact__icon" viewBox="0 0 24 24" aria-hidden="true"><path d="M2 5h20v14H2V5zm2 2v.4l8 5.2 8-5.2V7H4zm16 2.8-8 5.2-8-5.2V17h16V9.8z"/></svg>
        info@lanternkestrel.com
      </li>
    </ul>

    <address class="address" style="font-style: normal;">
      487 Mirella Ave.<br>
      Lake Havasu City, AZ 86519<br>
      www.lanternkestrel.com
    </address>
  </section>

  <section class="card card--back">
    <div class="back__pattern" role="img" aria-label="Repeating embossed brand pattern in dark charcoal tones"></div>
    <span class="back__mark">Lantern</span>
  </section>
</body>
</html>
```